Ancient Art and Artifact information website

Hello Designers,
We are starting up a new website who talk abut and discusses an ancient arts artifacts. We would covering a wide range of countries ranging from Egypt, Greece, India, Syria, Rome, etc. My website name Brisk Loom
Designs that fits with ancient theme and some kind of uniqueness would be accepted.
Requirements:
1) A home page design
2) Sub page design
3) A suitable logo
Sections can be added are featured ancient arts/places with short description followed by a more button, latest news, and comment section.
Add contents if you found relevant for this category of website. Ability to share the information through social media is desired.
Must be a responsive design. I look forward to designs which are mind blowing.
2 page

```html
<!DOCTYPE html>
<html lang="en">
<head>
<meta charset="utf-8">
<title>Brisk Loom — Ancient Art and Artifacts</title>
<link rel="stylesheet" href="https://fonts.googleapis.com/css2?family=Poppins:wght@300;400;500;600&family=PT+Serif:ital,wght@0,400;1,400&display=swap">
<style>
:root{
  --gold:#e2aa35;
  --ink:#1b1b1b;
  --text:#6f6f6f;
  --bar:#1f1f1f;
  --footer:#151515;
  --footer-bottom:#1a1a1a;
  --panel:#f0f0f0;
  --soft:#f8f8f8;
  --pill:#9d9d9d;
  --brand-dot:#7a5a45;
  --white:#ffffff;
}
*{margin:0;padding:0;box-sizing:border-box}
html,body{width:1200px;height:2296px;overflow:hidden;background:var(--white)}
body{position:relative;font-family:"Poppins",sans-serif;color:var(--ink)}
.abs{position:absolute}
.topbar{left:0;top:0;width:1200px;height:32px;background:var(--bar);color:var(--white);font-size:12px;font-weight:500}
.signin{left:86px;top:8px;display:flex;align-items:center;gap:10px}
.search{left:1085px;top:6px}
.header{left:0;top:32px;width:1200px;height:74px;background:var(--white)}
.brand{display:flex;align-items:center;gap:10px;color:var(--gold);font-weight:600;font-size:25px;letter-spacing:-.5px;white-space:nowrap}
.brand-dot{width:34px;height:34px;border-radius:50%;background:var(--brand-dot)}
.header-brand{left:81px;top:52px}
.footer-brand{left:81px;top:1953px}
.nav{top:62px;font-size:13px;font-weight:500;color:var(--ink)}
.nav.active{color:var(--gold)}
.hero{left:0;top:106px;width:1200px;height:393px}
.hero-panel{top:0;height:393px}
.hero-title{left:78px;top:134px;color:var(--white);font-weight:300;font-size:41px;line-height:64px}
.center{left:0;width:1200px;text-align:center}
.kicker{color:var(--gold);font-weight:300;font-size:21px}
.heading{font-weight:500;font-size:31px;letter-spacing:.5px}
.intro{top:628px;font-size:16px;line-height:26px;color:var(--text)}
.btn-outline{border:2px solid var(--ink);border-radius:6px;color:var(--gold);font-weight:600;font-size:17px;display:flex;align-items:center;justify-content:center}
.pager{background:#2b2b2b;display:flex;align-items:center;justify-content:space-around}
.card{top:946px;width:309px;height:427px;background:var(--panel);border-radius:5px;overflow:hidden}
.card-media{width:309px;height:225px}
.card-title{left:17px;top:237px;width:250px;font-size:16px;font-weight:400;line-height:23px;color:var(--ink)}
.card-text{left:18px;top:292px;width:270px;font-size:13.5px;line-height:23px;color:var(--text)}
.card-btn{left:17px;top:376px;width:93px;height:28px;background:var(--pill);border-radius:5px;color:var(--white);font-size:11.5px;font-weight:600;display:flex;align-items:center;justify-content:center}
.card-comments{left:179px;top:380px;display:flex;align-items:center;gap:14px;font-size:12.5px;color:var(--text)}
.news-band{left:0;top:1414px;width:1200px;height:493px;background:var(--soft)}
.date-day{left:615px;top:1568px;font-size:58px;font-weight:300;line-height:1}
.date-month{left:701px;top:1578px;font-size:18px;font-style:italic;font-weight:300;line-height:24px;color:#555}
.news-title{left:615px;top:1654px;font-size:15px;font-weight:500;letter-spacing:.3px}
.news-text{left:613px;top:1696px;width:505px;font-family:"PT Serif",serif;font-size:12.5px;line-height:23px;color:var(--text)}
.news-meta{left:613px;top:1760px;font-family:"PT Serif",serif;font-size:12.5px;color:#333;display:flex;align-items:center;gap:16px}
.footer{left:0;top:1907px;width:1200px;height:332px;background:var(--footer)}
.footer-text{left:80px;top:2018px;width:300px;font-family:"PT Serif",serif;font-size:12.5px;line-height:23px;color:#bdbdbd}
.social{top:2111px;width:35px;height:35px;border-radius:50%;background:#000}
.footer-head{top:1979px;color:var(--white);font-size:13px;font-weight:600;letter-spacing:.5px}
.footer-links{left:537px;top:2019px;list-style:none;font-size:12px;font-weight:500;color:var(--white);line-height:29px}
.footer-links .active{color:var(--gold)}
.email{left:880px;top:2053px;width:240px;height:39px;background:#000;color:#777;font-family:"PT Serif",serif;font-style:italic;font-size:11.5px;padding:12px 0 0 27px}
.subscribe{left:880px;top:2111px;width:240px;height:35px;background:var(--gold);color:var(--ink);font-size:11.5px;font-weight:600;display:flex;align-items:center;justify-content:center;letter-spacing:.5px}
.copyright{left:0;top:2239px;width:1200px;height:57px;background:var(--footer-bottom);border-top:1px solid #2a2a2a;color:#8a8a8a;font-family:"PT Serif",serif;font-size:12.5px;display:flex;align-items:center;justify-content:center}
</style>
</head>
<body>

<div class="abs topbar">
  <div class="abs signin">
    <svg width="14" height="14" viewBox="0 0 14 14"><circle cx="7" cy="4" r="3.3" fill="#fff"/><path d="M1 14c0-4 3-6 6-6s6 2 6 6z" fill="#fff"/></svg>
    <span>SIGN IN</span>
  </div>
  <svg class="abs search" width="18" height="18" viewBox="0 0 18 18"><circle cx="7.5" cy="7.5" r="5.5" stroke="#fff" stroke-width="2.2" fill="none"/><line x1="11.5" y1="11.5" x2="16" y2="16" stroke="#fff" stroke-width="2.4"/></svg>
</div>

<header class="abs header"></header>
<div class="abs brand header-brand"><span class="brand-dot"></span><span>Brisk Loom</span></div>
<nav>
  <span class="abs nav active" style="left:533px">HOME</span>
  <span class="abs nav" style="left:617px">ABOUT US</span>
  <span class="abs nav" style="left:727px">ANCIENT ART ARTIFACTS</span>
  <svg class="abs" style="left:894px;top:66px" width="8" height="6" viewBox="0 0 8 6"><path d="M1 1l3 3 3-3" stroke="#333" fill="none" stroke-width="1.2"/></svg>
  <span class="abs nav" style="left:931px">GALLERY</span>
  <span class="abs nav" style="left:1030px">LATEST NEWS</span>
</nav>

<section class="abs hero">
  <div class="abs hero-panel" style="left:0;width:496px;background:linear-gradient(135deg,#8a8782,#5f5c57 60%,#6e6a64)" role="img" aria-label="Carved stone relief panel"></div>
  <div class="abs hero-panel" style="left:496px;width:173px;background:linear-gradient(180deg,#b36c4c,#d8a57e 45%,#e6e1d6)" role="img" aria-label="Painted Egyptian wall figure"></div>
  <div class="abs hero-panel" style="left:669px;width:173px;background:linear-gradient(180deg,#dad6cf,#2e4f93 40%,#23397a 75%,#d9d4cc)" role="img" aria-label="Blue glass amphora on stand"></div>
  <div class="abs hero-panel" style="left:842px;width:174px;background:linear-gradient(180deg,#4a4542,#c8bba9 30%,#a99c8a)" role="img" aria-label="Stone statue of a standing pair"></div>
  <div class="abs hero-panel" style="left:1016px;width:184px;background:linear-gradient(180deg,#f2efea,#7a5a3d 40%,#4c3524 80%,#ece8e2)" role="img" aria-label="Ornate bronze pitcher"></div>
  <h1 class="abs hero-title">Lorem ipsum dolor<br>amet consect</h1>
  <svg class="abs" style="left:33px;top:210px" width="14" height="24" viewBox="0 0 14 24"><path d="M12 2L3 12l9 10" stroke="#fff" stroke-width="2.5" fill="none"/></svg>
  <svg class="abs" style="left:1162px;top:210px" width="14" height="24" viewBox="0 0 14 24"><path d="M2 2l9 10-9 10" stroke="#ddd" stroke-width="2.5" fill="none"/></svg>
</section>

<section>
  <p class="abs center kicker" style="top:537px">Welcome to</p>
  <h2 class="abs center heading" style="top:564px">BRISK LOOM</h2>
  <p class="abs center intro">Lorem ipsum dolor sit amet, consectetur adipiscing elit. Nunc sollicitudin ex id feugiat varius. Cras tincidunt<br>diam vel ex lacinia placerat. Mauris ultrices vulputate felis, eget convallis mi mattis ullamcorper.<br>Mauris vehicula libero ac sagittis euismod. Nullam bibendum congue placerat.<br>Fusce ornare scelerisque leo,</p>
  <div class="abs btn-outline" style="left:522px;top:761px;width:156px;height:44px">READ MORE</div>
</section>

<section>
  <p class="abs center kicker" style="top:843px">Ancient</p>
  <h2 class="abs center heading" style="top:870px">AN ANCIENT ARTS ARTIFACTS</h2>
  <div class="abs pager" style="left:1009px;top:853px;width:110px;height:42px">
    <svg width="10" height="10" viewBox="0 0 10 10"><path d="M8 1L2 5l6 4z" stroke="#e2aa35" fill="none" stroke-width="1.3"/></svg>
    <svg width="10" height="10" viewBox="0 0 10 10"><path d="M2 1l6 4-6 4z" stroke="#e2aa35" fill="none" stroke-width="1.3"/></svg>
  </div>

  <article class="abs card" style="left:84px">
    <div class="card-media" style="background:radial-gradient(circle at 50% 55%,#2f56b8,#1b3a8c 55%,#d8c22a 75%)" role="img" aria-label="Blue enamelled lidded jar"></div>
    <h3 class="abs card-title">Archeological excavations on the Iranian</h3>
    <p class="abs card-text">Lorem ipsum dolor sit amet, consect etur adipiscing elit. Nunc sollicitudin ex id feugiat varius. Cras tincidunt diam</p>
    <span class="abs card-btn">READ MORE</span>
    <span class="abs card-comments"><svg width="16" height="14" viewBox="0 0 16 14"><path d="M1 1h14v9H6l-4 3V10H1z" fill="#555"/></svg>17 comments</span>
  </article>

  <article class="abs card" style="left:458px">
    <div class="card-media" style="background:radial-gradient(ellipse at 50% 60%,#8a4a2c,#5a3020 45%,#c9c9cb 70%)" role="img" aria-label="Painted neck amphora"></div>
    <h3 class="abs card-title">Neck amphora (storage jar), ca. 620/615–595/590 b.c. Gree</h3>
    <p class="abs card-text">Lorem ipsum dolor sit amet, consect etur adipiscing elit. Nunc sollicitudin ex id feugiat varius. Cras tincidunt diam</p>
    <span class="abs card-btn">READ MORE</span>
    <span class="abs card-comments"><svg width="16" height="14" viewBox="0 0 16 14"><path d="M1 1h14v9H6l-4 3V10H1z" fill="#555"/></svg>17 comments</span>
  </article>

  <article class="abs card" style="left:810px">
    <div class="card-media" style="background:linear-gradient(135deg,#f4f2ef,#8c6a4a 45%,#5a4030 70%,#efece8)" role="img" aria-label="Bronze amphora pitcher detail"></div>
    <h3 class="abs card-title" style="top:248px">Rare Amphora Pitcher</h3>
    <p class="abs card-text">Lorem ipsum dolor sit amet, consect etur adipiscing elit. Nunc sollicitudin ex id feugiat varius. Cras tincidunt diam</p>
    <span class="abs card-btn">READ MORE</span>
    <span class="abs card-comments"><svg width="16" height="14" viewBox="0 0 16 14"><path d="M1 1h14v9H6l-4 3V10H1z" fill="#555"/></svg>17 comments</span>
  </article>
</section>

<section class="abs news-band"></section>
<section>
  <p class="abs kicker" style="left:81px;top:1452px">What Our Client Says</p>
  <h2 class="abs heading" style="left:81px;top:1479px;font-weight:600">LATEST NEWS</h2>
  <div class="abs pager" style="left:1009px;top:1462px;width:110px;height:43px">
    <svg width="10" height="10" viewBox="0 0 10 10"><path d="M8 1L2 5l6 4z" stroke="#e2aa35" fill="none" stroke-width="1.3"/></svg>
    <svg width="10" height="10" viewBox="0 0 10 10"><path d="M2 1l6 4-6 4z" stroke="#e2aa35" fill="none" stroke-width="1.3"/></svg>
  </div>
  <div class="abs" style="left:81px;top:1543px;width:505px;height:312px;background:linear-gradient(135deg,#c9b69a,#a8916f 50%,#cdbda3)" role="img" aria-label="Carved marble sarcophagus frieze"></div>
  <span class="abs date-day">08</span>
  <span class="abs date-month">March<br>2017</span>
  <h3 class="abs news-title">LOREM IPSUM DOLOR SIT AMET CONSECTETUR ADIPISCING ELIT</h3>
  <p class="abs news-text">Then one day he was shooting at some food and up through the ground came a crude oil that is so lets bubbling make the most of this beautiful day.</p>
  <p class="abs news-meta"><span>Marcus Hale</span><span style="display:flex;align-items:center;gap:8px"><svg width="14" height="12" viewBox="0 0 14 12"><path d="M1 1h12v7H5l-3 3V8H1z" stroke="#e2aa35" fill="none" stroke-width="1.3"/></svg>17 Comments</span></p>
  <div class="abs btn-outline" style="left:615px;top:1808px;width:156px;height:43px">READ MORE</div>
</section>

<footer>
  <div class="abs footer"></div>
  <div class="abs brand footer-brand"><span class="brand-dot"></span><span>Brisk Loom</span></div>
  <p class="abs footer-text">Then one day he was shooting at some food and up the ground came a crude oil day he was shooting at some food.</p>
  <span class="abs social" style="left:79px"></span>
  <span class="abs social" style="left:122px"></span>
  <span class="abs social" style="left:165px"></span>
  <span class="abs social" style="left:209px"></span>
  <span class="abs social" style="left:252px"></span>
  <h4 class="abs footer-head" style="left:537px">INFORMATION</h4>
  <ul class="abs footer-links">
    <li class="active">HOME</li>
    <li>ABOUT US</li>
    <li>ANCIENT ART ARTIFACTS</li>
    <li>GALLERY</li>
    <li>&nbsp;LATEST NEWS</li>
  </ul>
  <h4 class="abs footer-head" style="left:880px">NEWSLETTER</h4>
  <div class="abs email">Your Email id</div>
  <div class="abs subscribe">SUBCRIBE</div>
  <div class="abs copyright">Copyrights © 2016. All Rights Reserved</div>
</footer>

</body>
</html>
```